tolv Marketing Brochure for construction of multi-million dollar homes in the Caribbean

Design a marketing brochure for a construction company operating in the Caribbean for ultra high-end signature homes and villas. Target audience is ultra high net worth individuals, families, international property developers and hotel chains. We have provided an our marketing brochure for reference but would like a totally new look and feel with updated wording and photos (also provided). The company logo of light and dark blue circles and 'tolv' with the 's' in superscript must feature throughout. Further information can be extracted from the company's website: tolvharbour.example. Depending on how this goes there may be additional projects such as website and log redesign. Thanks!

Target Market(s)

Target audience is ultra high net worth individuals, families, international property developers and hotel chains.

Font styles to use
Other font styles liked:
• see logo for desired phones

Colors
3aa7d7
0655a3
85cae6
3176b5
85acd3
33a6d7
cee9f5
cedeed

Requirements
Must have
• Detailed company info including projects and employee profiles - must be bold, brilliant and eye-catching.
Nice to have
• Colour
Should not have
• Too much info.

```html
<!DOCTYPE html>
<html lang="en">
<head>
<meta charset="utf-8">
<title>tolv brochure</title>
<link href="https://fonts.googleapis.com/css2?family=Montserrat:wght@400;600;700&family=Open+Sans:wght@400;600&display=swap" rel="stylesheet">
<style>
  :root {
    --canvas: #e4e5e7;
    --paper: #ffffff;
    --navy: #27348f;
    --brand-dark: #0655a3;
    --brand-mid: #3176b5;
    --sky: #3aa7d7;
    --sky-soft: #85cae6;
    --ice: #cee9f5;
    --mist: #cedeed;
    --ink: #2a2d3a;
    --frame: #8d909a;
    --url: #85cae6;
  }
  * { box-sizing: border-box; margin: 0; padding: 0; }
  html, body { width: 1200px; height: 900px; overflow: hidden; }
  body {
    background: var(--canvas);
    font-family: "Open Sans", Arial, sans-serif;
    color: var(--ink);
    position: relative;
  }
  .page {
    position: absolute;
    width: 560px;
    height: 340px;
    background: var(--paper);
    overflow: hidden;
    box-shadow: 0 6px 18px rgba(0,0,0,0.18);
  }
  .page__sky {
    position: absolute; left: 0; top: 0; width: 100%; height: 120px;
    background: linear-gradient(180deg, var(--sky-soft) 0%, var(--ice) 55%, var(--paper) 100%);
  }
  .page__band {
    position: absolute; left: 0; bottom: 0; width: 100%; height: 62px;
    background: var(--navy);
  }
  .page__rule {
    position: absolute; left: 10px; right: 10px; bottom: 10px; top: 180px;
    border: 1px solid var(--frame);
    border-top: none;
  }
  .page__url {
    position: absolute; right: 22px; bottom: 14px;
    font-family: "Montserrat", Arial, sans-serif;
    font-size: 11px; letter-spacing: 0.5px;
    color: var(--url);
  }
  .photo {
    position: absolute;
    border: 5px solid var(--paper);
    outline: 1px solid var(--frame);
    box-shadow: 0 1px 3px rgba(0,0,0,0.2);
  }
  .photo--villa-day { background: linear-gradient(180deg, #4a9ad8 0%, #8fc7e8 35%, #b27a4c 60%, #3d7a34 100%); }
  .photo--lounge { background: linear-gradient(180deg, #d9d2c3 0%, #8cc0e0 45%, #cbbfa9 100%); }
  .photo--terrace { background: linear-gradient(180deg, #9a6a45 0%, #5fa9c9 50%, #c6b69a 100%); }
  .photo--bath { background: linear-gradient(180deg, #e8e3d8 0%, #f4f1ea 50%, #c9b89a 100%); }
  .photo--villa-dusk { background: linear-gradient(180deg, #8a96a3 0%, #6f6a58 45%, #7a5a36 75%, #3b4a2c 100%); }
  .photo--pool { background: linear-gradient(180deg, #3a4658 0%, #c99a52 45%, #3c9cc4 100%); }
  .photo--suite { background: linear-gradient(180deg, #dfe4e6 0%, #9bbfa8 40%, #f2f2f0 100%); }
  .photo--bath-sea { background: linear-gradient(90deg, #efe9df 0%, #f5f2ec 55%, #5ea9d6 80%, #2f7fbf 100%); }
  .photo--deck { background: linear-gradient(180deg, #7d5a3c 0%, #3f82b8 45%, #2a5e94 100%); }

  .cover { left: 320px; top: 50px; }
  .brand {
    position: absolute; left: 28px; top: 34px;
    display: flex; align-items: center; gap: 12px;
  }
  .brand__square {
    width: 30px; height: 30px;
    background: var(--brand-mid);
  }
  .brand__name {
    font-family: "Montserrat", Arial, sans-serif;
    font-weight: 700; font-size: 44px; line-height: 1;
    color: var(--navy);
  }
  .brand__tagline {
    position: absolute; left: 70px; top: 90px;
    font-family: "Montserrat", Arial, sans-serif;
    font-size: 9px; color: var(--navy); letter-spacing: 1px;
    text-transform: uppercase;
  }

  .spread-left { left: 40px; top: 430px; }
  .spread-right { left: 600px; top: 430px; }
  .spread-fold {
    position: absolute; left: 599px; top: 430px; width: 2px; height: 340px;
    background: linear-gradient(90deg, rgba(0,0,0,0.18), rgba(0,0,0,0));
  }
  .intro { position: absolute; left: 24px; top: 18px; width: 510px; }
  .intro__title {
    font-family: "Montserrat", Arial, sans-serif;
    font-weight: 700; font-size: 14px; color: var(--navy);
    margin-bottom: 6px;
  }
  .intro__body, .about__body {
    font-size: 8.6px; line-height: 1.4; color: var(--ink);
  }
  .about { position: absolute; left: 24px; top: 18px; width: 512px; }
  .about__body + .about__body { margin-top: 6px; }
</style>
</head>
<body>

  <section class="page cover">
    <div class="page__sky"></div>
    <div class="page__band"></div>
    <div class="brand">
      <span class="brand__square"></span>
      <span class="brand__name">tolv</span>
    </div>
    <p class="brand__tagline">signature homes &amp; villas</p>
    <div class="photo photo--villa-day" style="left:20px; top:120px; width:350px; height:180px;" role="img" aria-label="Photo of a timber and stone villa entrance among palm trees"></div>
    <div class="photo photo--lounge" style="left:385px; top:20px; width:155px; height:88px;" role="img" aria-label="Photo of a bright living room opening onto the sea"></div>
    <div class="photo photo--terrace" style="left:385px; top:118px; width:155px; height:80px;" role="img" aria-label="Photo of a covered pool terrace with seating"></div>
    <div class="photo photo--bath" style="left:385px; top:208px; width:155px; height:86px;" role="img" aria-label="Photo of a bathroom with freestanding tub"></div>
    <span class="page__url">www.tolvharbour.example</span>
  </section>

  <section class="page spread-left">
    <div class="page__sky"></div>
    <div class="page__band"></div>
    <div class="page__rule"></div>
    <div class="intro">
      <h1 class="intro__title">Welcome to tolv...professionals in building</h1>
      <p class="intro__body">If you are looking to build your ultimate dream home in your own piece of paradise, tolv can make it a reality. We guide you through every stage of the building process, from planning and design to completion. Specialising in luxurious private residences throughout the Caribbean, tolv has built an enviable portfolio of breathtaking villas and opulent homes for extremely satisfied clientele.</p>
    </div>
    <div class="photo photo--villa-dusk" style="left:22px; top:110px; width:310px; height:196px;" role="img" aria-label="Photo of a stone villa lit at dusk on a hillside"></div>
    <div class="photo photo--pool" style="left:345px; top:118px; width:190px; height:82px;" role="img" aria-label="Photo of a villa pool at night"></div>
    <div class="photo photo--suite" style="left:345px; top:208px; width:190px; height:80px;" role="img" aria-label="Photo of a bedroom suite with garden views"></div>
    <span class="page__url">www.tolvharbour.example</span>
  </section>

  <section class="page spread-right">
    <div class="page__sky"></div>
    <div class="page__band"></div>
    <div class="page__rule"></div>
    <div class="about">
      <p class="about__body">tolv caters to clients who are not able to be present for the duration of their project and therefore require building professionals to represent their best interests. From the beginning of the process, our services will help you understand in detail how we get to the end product with the agreed original parameters.</p>
      <p class="about__body">Our team consists largely of British and American personnel with support from local communities and consists of Project Managers, Chartered Builders, Civil and Structural Engineers, Chartered Quantity Surveyors, Estimators and Qualified Electrical &amp; Mechanical Engineers.</p>
    </div>
    <div class="photo photo--bath-sea" style="left:22px; top:120px; width:380px; height:186px;" role="img" aria-label="Photo of a marble bathroom with tub and ocean view"></div>
    <div class="photo photo--deck" style="left:412px; top:128px; width:126px; height:86px;" role="img" aria-label="Photo of a terrace overlooking the sea"></div>
    <span class="page__url">www.tolvharbour.example</span>
  </section>
  <div class="spread-fold"></div>

</body>
</html>
```